Harbor Valley Pride Sponsorship

Harbor Valley Pride is looking for an updated sponsorship package design – included in the shared information is our sponsorship packaged used in 2017, 2018, and 2019.

The mission of Harbor Valley Pride is to create opportunities for integrating and promoting visibility for the lesbian. gay, bisexual and transgender community; promoting equal rights and diversity through public education and the arts; provide safe opportunities and venues for people to come out with the ability to express and celebrate their sexual identities.

Some images (because of their size) are not allowed to be uploaded... use the following link to access the full library of images, reference documents, and the full outline: https://files.examplecloud.net/share/7kQmZ2tVx9LpR4nWc8Hs3dYb

Sponsorship packet design details:
Final file type: .pdf and/or .ai/.eps
Orientation: Preferably landscape but not opposed to a portrait design.
Page count: estimated 6 with current content (not opposed to 8 pages)
Size: 8.5”x11”
Full bleed

Images:
Images for this design are shared in a folder “images for use in sponsorship packet” – please feel free to choose them as you see fit and we can make any notes after the first draft.

Creative Reference:
Additionally, provided are a few sponsorship packages that we like and feel that you might be able to take inspiration from – these are in a folder named “sponsorship packets we like”
Updates

I've updated all of the details of this project and would like to have completed asap. Thank you.

Target Market(s)

Primarily our target market is local and regional businesses that are interested in supporting JoyFair through sponsorship or might be interested in advertising opportunities.

Industry/Entity Type

LGBT

Font styles to use
Serif
Sans Serif

Colors

Designer to choose colors to be used in the design.

Requirements
Must have
• All sponsorship details

```html
<!DOCTYPE html>
<html lang="en">
<head>
<meta charset="utf-8">
<title>Harbor Valley Pride Sponsorship – Pages 4 to 6</title>
<link rel="stylesheet" href="https://fonts.googleapis.com/css2?family=Inter:wght@400;500;600&family=Rubik:wght@500;700;800&display=swap">
<style>
  :root{
    --board:#f7f7f7;
    --board-light:#ffffff;
    --ink:#222222;
    --orange:#f7922a;
    --yellow:#fdbd36;
    --green:#7ab342;
    --blue:#1e7cc8;
    --sky:#3b8ff0;
    --violet:#6a479a;
    --violet-deep:#5b3d8c;
    --red:#f0443f;
    --title:#6a3e98;
  }
  *{box-sizing:border-box;margin:0;padding:0}
  html,body{width:1200px;height:2325px;overflow:hidden;background:var(--board)}
  body{position:relative;font-family:"Inter",Arial,sans-serif;color:var(--ink)}
  .board-bg{position:absolute;inset:0}
  .page-label{position:absolute;left:345px;font-family:"Inter",Arial,sans-serif;font-size:21px;font-weight:400;color:#333;letter-spacing:.2px}
  .page{position:absolute;left:497px;width:499px;height:640px;background:#fff;overflow:hidden;box-shadow:0 10px 30px rgba(0,0,0,.12)}
  .abs{position:absolute}
  .photo{position:absolute}
  .badge{position:absolute;border-radius:50%;display:flex;flex-direction:column;align-items:center;justify-content:center;color:#fff;font-family:"Rubik",Arial,sans-serif;font-weight:800;line-height:1.05;text-align:center;box-shadow:0 0 0 5px rgba(255,255,255,.85),0 6px 14px rgba(0,0,0,.18)}
  .badge .tier{font-size:19px;letter-spacing:.3px}
  .badge .price{font-size:16px;font-weight:700}
  .perks{position:absolute;list-style:none;font-size:7.6px;line-height:14.3px;font-weight:500}
  .perks li{position:relative;padding-left:11px}
  .perks li::before{content:"";position:absolute;left:0;top:5px;width:3px;height:3px;border:1px solid var(--dot,#f7922a);border-radius:50%}
  .ring{border-radius:50%;border:3px solid #fff;box-shadow:0 0 0 2px #e94d8b,0 0 0 4px #fdbd36}
  .prod-title{position:absolute;left:41px;top:36px;font-family:"Rubik",Arial,sans-serif;font-weight:700;font-size:26px;line-height:24px;color:var(--title)}
  .pill{position:absolute;height:26px;border-radius:13px;color:#fff;font-size:7.6px;font-weight:600;display:flex;align-items:center;justify-content:center;text-align:center;line-height:9px;padding:0 10px}
  .pill.dark{color:#3a2a00}
  .prod-text{position:absolute;font-size:7px;line-height:11px}
  .rule{position:absolute;left:0;right:0;border-top:1px dashed #e3e3e3}
  .inkind h2{font-family:"Rubik",Arial,sans-serif;font-weight:800;font-size:15px;line-height:18px;color:#1b1b1b}
  .inkind h3{font-family:"Inter",Arial,sans-serif;font-weight:600;font-size:10.5px;margin-top:16px;color:#1b1b1b;letter-spacing:.4px}
  .inkind p{font-size:7px;line-height:12px;color:#fff}
</style>
</head>
<body>
<svg class="board-bg" width="1200" height="2325" viewBox="0 0 1200 2325" aria-hidden="true">
  <polygon points="0,1175 1200,1000 1200,2140 0,1995" fill="var(--board-light)"/>
</svg>

<div class="page-label" style="top:607px">PAGE 4</div>
<div class="page-label" style="top:1393px">PAGE 5</div>
<div class="page-label" style="top:2121px">PAGE 6</div>

<!-- PAGE 4 -->
<section class="page" style="top:79px">
  <div class="photo" role="img" aria-label="Colourful handwritten pride message cards" style="left:0;top:0;width:499px;height:156px;clip-path:polygon(0 0,100% 0,100% 100%,0 80%);background:linear-gradient(100deg,#e8304a 0%,#f2d33c 25%,#8a4fc4 45%,#e84a3a 65%,#f7922a 85%,#f4d23c 100%)"></div>
  <div class="badge" style="left:292px;top:64px;width:100px;height:100px;background:var(--orange)"><span class="tier">ORANGE</span><span class="price">$10,000</span></div>
  <ul class="perks" style="left:25px;top:145px;width:240px;--dot:var(--orange)">
    <li>10 x 20 premium vendor booth during JoyFair</li>
    <li>Premium placement in the Lantern Glow Parade</li>
    <li>Use of the annual theme and HV Pride logo</li>
    <li>Click-thru logo placement on sponsorship web page</li>
    <li>Admission for six to the HV Pride VIP Party</li>
    <li>Name/logo displayed at official Harbor Valley Pride events</li>
    <li>Opportunity for ad placement on hvpride.example homepage</li>
    <li>Opportunity to table and promote brand at key Countdown to Pride events</li>
  </ul>
  <ul class="perks" style="left:264px;top:189px;width:225px;--dot:var(--orange)">
    <li>One dedicated social media post (sponsor responsible for marketing materials)</li>
    <li>Click-thru logo included in one Pre-Pride E-Blast</li>
    <li>One half-page ad placement in the official HV Pride Guide*</li>
  </ul>

  <div class="abs" style="left:0;top:293px;width:499px;height:163px;background:var(--yellow)"></div>
  <div class="photo" role="img" aria-label="Young child holding a small rainbow flag at the parade" style="left:0;top:293px;width:144px;height:163px;background:linear-gradient(160deg,#c9c2b8,#8f8a86 60%,#c85a6a)"></div>
  <div class="badge" style="left:370px;top:270px;width:84px;height:84px;background:var(--yellow)"><span class="tier" style="font-size:16px">YELLOW</span><span class="price" style="font-size:14px">$10,000</span></div>
  <ul class="perks" style="left:162px;top:325px;width:320px;--dot:#7a4a00;color:#fff">
    <li>10 x 20 premium vendor booth during JoyFair</li>
    <li>Premium placement in the Lantern Glow Parade</li>
    <li>Use of the annual theme and HV Pride logo</li>
    <li>Click-thru logo placement on sponsorship web page</li>
    <li>Admission for four to the HV Pride VIP Party</li>
    <li>Name/logo displayed at official Harbor Valley Pride events</li>
    <li>Opportunity for ad placement on hvpride.example homepage</li>
    <li>Opportunity to table and promote brand at key Countdown to Pride events</li>
  </ul>

  <div class="photo" role="img" aria-label="Parade performer with a rainbow umbrella" style="left:317px;top:456px;width:182px;height:184px;background:linear-gradient(135deg,#e84a3a,#f7c33c 35%,#4aa04a 60%,#3a6fd0 80%,#8a4fc4)"></div>
  <div class="badge" style="left:251px;top:496px;width:92px;height:92px;background:var(--green)"><span class="tier" style="font-size:17px">GREEN</span><span class="price">$5,000</span></div>
  <ul class="perks" style="left:25px;top:500px;width:240px;--dot:var(--green)">
    <li>10 x 10 vendor booth during JoyFair</li>
    <li>Placement in the Lantern Glow Parade</li>
    <li>Use of the annual theme and HV Pride logo</li>
    <li>Click-thru logo placement on sponsorship web page</li>
    <li>Admission for four to the HV Pride VIP Party</li>
    <li>Name/logo displayed at official Harbor Valley Pride events</li>
    <li>Opportunity for ad placement on hvpride.example homepage</li>
  </ul>
</section>

<!-- PAGE 5 -->
<section class="page" style="top:837px">
  <div class="photo ring" role="img" aria-label="Friends celebrating with rainbow fans and flags" style="left:284px;top:-56px;width:260px;height:260px;background:linear-gradient(135deg,#d94a4a,#3a6fd0 45%,#f7c33c 75%,#7ab342)"></div>
  <div class="badge" style="left:270px;top:84px;width:98px;height:98px;background:var(--blue);transform:rotate(8deg)"><span class="tier" style="font-size:19px">BLUE</span><span class="price">$3,000</span></div>
  <ul class="perks" style="left:30px;top:51px;width:240px;--dot:var(--blue)">
    <li>10 x 10 vendor booth during JoyFair</li>
    <li>Placement in the Lantern Glow Parade</li>
    <li>Use of the annual theme and HV Pride logo</li>
    <li>Static logo placement on sponsorship web page</li>
    <li>Admission for two at the HV Pride VIP Party</li>
    <li>Name/logo displayed to official Harbor Valley Pride events</li>
  </ul>

  <svg class="abs" style="left:0;top:0" width="499" height="640" aria-hidden="true">
    <polygon points="0,263 499,200 499,447 0,379" fill="var(--violet)"/>
    <polygon points="0,379 499,447 499,640 0,640" fill="var(--yellow)"/>
  </svg>
  <div class="photo ring" role="img" aria-label="Marchers holding a hand-painted sign with rainbow banners" style="left:25px;top:159px;width:176px;height:176px;background:linear-gradient(150deg,#7fa8d8,#e8e0d0 45%,#e84a3a 70%,#8a4fc4)"></div>
  <div class="badge" style="left:223px;top:208px;width:80px;height:80px;background:var(--violet-deep)"><span class="tier" style="font-size:16px">VIOLET</span><span class="price" style="font-size:14px">$1,500</span></div>
  <ul class="perks" style="left:241px;top:316px;width:230px;--dot:#fff;color:#fff">
    <li>10 x 10 vendor booth during JoyFair</li>
    <li>Use of the annual theme and HV Pride logo</li>
    <li>Static logo placement on sponsorship web page</li>
    <li>Admission for two to the HV Pride VIP Party</li>
  </ul>

  <div class="photo ring" role="img" aria-label="Performer on stage before a large festival crowd" style="left:321px;top:399px;width:150px;height:150px;background:linear-gradient(170deg,#8fb8e0,#b85a4a 45%,#d8c8b8 70%,#7a6a8a)"></div>
  <div class="abs inkind" style="left:34px;top:410px;width:340px">
    <h2>IN-KIND<br>SPONSORSHIPS</h2>
    <h3>HOST HOTEL</h3>
    <p>Sponsors should have the ability to provide 8-10 comp rooms for 2 nights.<br>Become our host hotel and brand yourself as the JoyFair travel hub.</p>
    <h3>RAFFLE / AUCTION ITEMS</h3>
    <p>Sponsors should have the ability to provide 8-10 comp rooms for 2 nights.<br>Become our host hotel and brand yourself as the JoyFair travel hub.</p>
    <h3>CAR DEALERSHIP</h3>
    <p style="width:420px">Sponsor should be able to provide 5-10 vehicles to be used in the Lantern Glow Parade.<br>Sponsors must provide/install any branding on the vehicle.</p>
  </div>
</section>

<!-- PAGE 6 -->
<section class="page" style="top:1592px">
  <h1 class="prod-title">Production<br>Partnership</h1>
  <div class="rule" style="top:74px;left:200px"></div>
  <div class="pill" style="left:310px;top:61px;width:160px;background:var(--sky)">KidZone Partnership &nbsp;|&nbsp; $3,500</div>
  <p class="prod-text" style="left:41px;top:107px;width:415px;text-align:justify">For over 40 years, Harbor Valley JoyFair has opened its gates to everyone. The Harbor Valley Pride KidZone is an area where families can go and have their own Pride experience. Packed with fun games, interactive performances and more! This production partnership allows businesses to brand the KidZone with their business and funding will be used to pay for programing and logistics related to the Harbor Valley Pride KidZone production.</p>

  <div class="rule" style="top:178px"></div>
  <div class="pill" style="left:31px;top:165px;width:160px;background:var(--green)">Mainstage Partnership<br>$20,000 – $30,000</div>
  <p class="prod-text" style="left:41px;top:210px;width:415px;text-align:justify">Brand our mainstage and have your business front and center for over 100,000 people to see. The opportunities for this production partnership are endless and really allow businesses to benefit from our live local and regional acts and the diverse exposure that they bring.</p>

  <div class="rule" style="top:256px"></div>
  <div class="pill dark" style="left:310px;top:243px;width:160px;background:var(--yellow)">'Starfall' Fireworks Display<br>Partnership | $8,000 – $15,000</div>
  <p class="prod-text" style="left:200px;top:287px;width:256px;text-align:right">Receive yellow level sponsorship benefits and make the first Starfall Fireworks Display possible through this unique partnership.</p>

  <div class="rule" style="top:324px"></div>
  <div class="pill" style="left:31px;top:311px;width:160px;background:var(--orange)">Parade Square Partnership<br>$6,500</div>
  <p class="prod-text" style="left:41px;top:352px;width:240px">The valley's only lantern-lit evening Pride Parade, brand your business with this production partnership and receive exposure to over 100,000 people in Downtown, Harbor City.</p>

  <div class="rule" style="top:390px"></div>
  <div class="pill" style="left:310px;top:377px;width:160px;background:var(--red)">Volunteer Wellness &amp;<br>Hospitality Partnership | $10,000</div>
  <p class="prod-text" style="left:41px;top:421px;width:415px;text-align:right">Help us say thank you to the 250+ volunteers that make Harbor Valley JoyFair and the Lantern Glow Parade possible. This production partnership allows businesses to brand the volunteer hospitality area (a 20' x 20' centrally located tented space) and the option of including their name/logo* on the rear side of volunteer t-shirts. Funding through this partnership also allows us to provide sunscreen, water, snack, lunch and more for our team!</p>
  <p class="prod-text" style="left:250px;top:472px;width:206px;text-align:right;font-style:italic;font-size:6.5px">*logos are screen printed in one color, multiple colors are available at increased cost.</p>

  <div class="photo" role="img" aria-label="Two drag performers before a festival crowd with the city skyline behind" style="left:0;top:462px;width:499px;height:178px;clip-path:polygon(0 0,100% 30%,100% 100%,0 100%);background:linear-gradient(180deg,#a8c8e8 0%,#c8d8e8 35%,#8a6a7a 60%,#c87a6a 80%,#6a5a7a 100%)"></div>
</section>
</body>
</html>
```